Business Card phone number change

This one should be easy, and I've committed to pay even is takes you minutes to complete.
I have a completed business card for which I just need a phone number changed. It needs to be done asap (within hours) so I can have it printed today. I have the card design and everything. Literally just need phone number changed and positioned in correct place. If you can do it, let me know.
The card was originally designed with 3.62” x 2.12” . It was modified to US standard 3.5” x 2” (which is how I need it).

On the file named "Final TK Partners card size" the NY number should read +1 555 318 4720" rather than the 555 407 2983 number that is there. If you can do let, let me now ASAP.
Updates

Project Deadline Extended Reason: The deadling is today, 4 hours from initial posting. Short window as all that needs to be changed is the phone number and I need to print a stack today before meeting. Added Saturday, January 14, 2017

Industry/Entity Type

Business

Requirements
Must have
• The correct NY phone number of +1 555 318 4720
• Everything else stays the same.

```html
<!DOCTYPE html>
<html lang="en">
<head>
<meta charset="utf-8">
<title>TK Partners – Business Card</title>
<link rel="stylesheet" href="https://fonts.googleapis.com/css2?family=PT+Serif:wght@400;700&display=swap">
<style>
  :root {
    --navy: #2e4b6c;
    --ink: #3d3d3d;
    --label: #9a9a9a;
    --card-border: #b9b9b9;
    --page: #ffffff;
  }
  html, body {
    margin: 0;
    width: 1200px;
    height: 848px;
    overflow: hidden;
    background: var(--page);
    font-family: "PT Serif", Georgia, serif;
  }
  .card {
    position: absolute;
    left: 255px;
    top: 225px;
    width: 690px;
    height: 396px;
    box-sizing: border-box;
    border: 1px solid var(--card-border);
    background: #fff;
  }
  .brand-mark {
    position: absolute;
    left: 353px;
    top: 38px;
    width: 80px;
    height: 80px;
    border-radius: 50%;
    background: var(--navy);
  }
  .brand-name {
    position: absolute;
    right: 43px;
    top: 72px;
    margin: 0;
    font-size: 34px;
    line-height: 1;
    font-weight: 700;
    color: var(--navy);
    white-space: nowrap;
  }
  .address {
    position: absolute;
    right: 43px;
    top: 113px;
    margin: 0;
    font-style: normal;
    font-size: 18px;
    line-height: 24px;
    color: var(--ink);
    text-align: right;
  }
  .person-name {
    position: absolute;
    left: 137px;
    top: 171px;
    margin: 0;
    font-size: 27px;
    line-height: 1;
    font-weight: 700;
    color: var(--navy);
    word-spacing: 3px;
  }
  .person-title {
    position: absolute;
    left: 137px;
    top: 200px;
    margin: 0;
    font-size: 22px;
    line-height: 1;
    color: var(--ink);
  }
  .rule {
    position: absolute;
    left: 128px;
    right: -1px;
    height: 5px;
    background: var(--navy);
  }
  .rule-top { top: 236px; }
  .rule-bottom { top: 350px; }
  .contact-list {
    position: absolute;
    left: 0;
    top: 252px;
    margin: 0;
    font-size: 18px;
    line-height: 22.7px;
  }
  .contact-row { display: flex; }
  .contact-row dt {
    width: 123px;
    text-align: right;
    color: var(--label);
  }
  .contact-row dd {
    margin: 0 0 0 15px;
    color: var(--navy);
  }
</style>
</head>
<body>
  <article class="card">
    <div class="brand-mark" aria-hidden="true"></div>
    <p class="brand-name">TK Partners</p>
    <address class="address">72 Orchard Street<br>Brooklyn, NY 11201</address>

    <h1 class="person-name">Elan Marsh</h1>
    <p class="person-title">Healthcare Consultant</p>

    <div class="rule rule-top"></div>
    <dl class="contact-list">
      <div class="contact-row"><dt>New York:</dt><dd>+1 555 318 4720</dd></div>
      <div class="contact-row"><dt>Madrid:</dt><dd>+34 611 204 857</dd></div>
      <div class="contact-row"><dt>Email:</dt><dd>emarsh@tkpartners.com</dd></div>
      <div class="contact-row"><dt>Web:</dt><dd>www.tkpartners.com</dd></div>
    </dl>
    <div class="rule rule-bottom"></div>
  </article>
</body>
</html>
```